Flyer Design Project

We are a start-up real estate brokerage looking to attract new agents. Our business relies heavily on technology to help give agents more time to spend with clients. Our model is also different from a typical broker in that we do not take a percentage of commission from each sale an agent makes. Instead we charge a simple flat monthly fee and the agent keeps 100% of the commission the earn.
The ideal flyer will be pleasing to the eye, should probably have some appropriate graphics, use our logo and project a modern yet sophisticated company image. This is and advertising flyer that will be followed up with a more detailed brochure (later project).
Updates

While I like the initial design I was looking for more of a change from my design.  Here are some clarifications:

The design should not included the "click" option so it can be used online or in print.  Instead include the site corvelliahomes.com/careers

I want more of a list of features with less description.  The list should have:
- Deal Tracker included
- No Commission Split
- No Floor Time... Leads sent directly to you
- E & O Insurance included
- All your listings showcased on Homefinda.com
- Showing appointment solution.

Some description of each can be included but less of a question answer style than what I originally had.
It does not need to be a straight list, the items all need to be mentioned somewhere on the flyer but not necessarily in a list style.
Maybe an image of business meeting or greeting (agent joining).

Please do not hesitate to ask questions for clarification

The image of meeting or greeting is optional - you choose what you think is best.
Also, use of the "About Us" that was uploaded my be a good idea.  - I'm not sure on this either

Target Market(s)

current real estate agents and people considering a real estate career

Industry/Entity Type

Real Estate

Requirements
Must have
• Should list that we include "Deal Tracker" which is considered the top program for real estate agents (info and logos can be found at dealtracker.com)
Should highlight our low cost structure ($350 per month) and no transaction fees.
Should highlight that no office time is required. We provide virtual office solutions to save time.
Our contact number (555) 482-9167 ext. 204
Nice to have
• Any other additional information from the attached flyers (which should not be used as a template as they all need to be designed in a later project).

```html
<!DOCTYPE html>
<html lang="en">
<head>
<meta charset="utf-8">
<title>Corvellia Homes – Agent Recruiting Flyer</title>
<link href="https://fonts.googleapis.com/css2?family=EB+Garamond:ital,wght@0,400;1,400&family=Lato:wght@300;400;700&display=swap" rel="stylesheet">
<style>
  :root {
    --moss: #7c9b47;
    --moss-dark: #5f7d33;
    --moss-text: #86ab45;
    --gold: #a8821f;
    --gold-line: #b39446;
    --ink: #2e2e2e;
    --paper: #ffffff;
    --bullet: #8ab04a;
    --dot: #6b1f1f;
  }
  * { margin: 0; padding: 0; box-sizing: border-box; }
  html, body { width: 927px; height: 1200px; overflow: hidden; background: var(--paper); }
  .flyer { position: relative; width: 927px; height: 1200px; overflow: hidden; background: var(--paper); color: var(--ink); font-family: "Lato", sans-serif; }

  .header-texture {
    position: absolute; left: 0; top: 0; width: 927px; height: 492px;
    background: linear-gradient(135deg, #86a552 0%, var(--moss) 45%, var(--moss-dark) 100%);
  }
  .audience {
    position: absolute; top: 30px; width: 100%; text-align: center; white-space: nowrap;
    font-family: "EB Garamond", serif; color: var(--paper); font-size: 35px; letter-spacing: 1px;
  }
  .audience em { font-style: italic; font-size: 44px; }
  .rule-white { position: absolute; left: 0; width: 927px; height: 1.5px; background: rgba(255,255,255,0.85); }
  .headline {
    position: absolute; top: 96px; width: 100%; text-align: center; white-space: nowrap;
    font-family: "Lato", sans-serif; font-weight: 300; color: var(--paper);
    font-size: 116px; line-height: 120px; letter-spacing: 0;
  }
  .offer {
    position: absolute; top: 248px; width: 100%; text-align: center; white-space: nowrap;
    font-family: "EB Garamond", serif; color: var(--paper); font-size: 32px; letter-spacing: 0.5px;
  }
  .offer em { font-style: italic; font-size: 42px; }
  .offer .divider { margin: 0 18px; }

  .hero-photo {
    position: absolute; left: 54px; top: 319px; width: 830px; height: 458px;
    background: linear-gradient(180deg, #a9c4dc 0%, #cfdbe2 30%, #7f9a4e 55%, #5b8a2c 78%, #74a83a 100%);
  }

  .features {
    position: absolute; left: 54px; top: 821px; width: 830px; height: 126px;
    border-top: 1.5px solid var(--gold-line); border-bottom: 1.5px solid var(--gold-line);
  }
  .feature-list { position: absolute; top: 20px; list-style: none; font-size: 22px; line-height: 30px; white-space: nowrap; }
  .feature-list li { position: relative; padding-left: 18px; }
  .feature-list li::before { content: ""; position: absolute; left: 0; top: 12px; width: 8px; height: 8px; border-radius: 50%; background: var(--bullet); }
  .feature-list.left { left: 24px; }
  .feature-list.right { left: 424px; }

  .pricing-band {
    position: absolute; left: 0; top: 989px; width: 927px; height: 53px;
    background: var(--gold); color: var(--paper); white-space: nowrap;
    display: flex; align-items: center; justify-content: center; gap: 16px;
    font-size: 23px; letter-spacing: 0.6px;
  }
  .pricing-band .sep { width: 6px; height: 6px; border-radius: 50%; background: var(--dot); }

  .contact { position: absolute; left: 54px; top: 1088px; font-size: 17px; letter-spacing: 3px; line-height: 30px; white-space: nowrap; }
  .contact .link { color: var(--moss-text); font-weight: 700; font-size: 22px; letter-spacing: 0.3px; }
  .contact .phone { color: var(--moss-text); font-weight: 700; font-size: 22px; letter-spacing: 0.3px; }

  .brand { position: absolute; left: 465px; top: 1100px; display: flex; align-items: center; gap: 14px; white-space: nowrap; }
  .brand-mark { width: 40px; height: 40px; background: var(--dot); }
  .brand-name { font-family: "EB Garamond", serif; font-size: 34px; color: var(--ink); letter-spacing: 1px; }
</style>
</head>
<body>
<div class="flyer">
  <div class="header-texture" role="img" aria-label="Green woodgrain texture background"></div>
  <div class="audience">EXPERIENCED <em>and</em> NEW AGENTS</div>
  <div class="rule-white" style="top:89px"></div>
  <div class="headline">COME JOIN US!</div>
  <div class="rule-white" style="top:225px"></div>
  <div class="offer">DEAL TRACKER <em>included</em><span class="divider">|</span>NO COMMISSION SPLIT</div>

  <div class="hero-photo" role="img" aria-label="Large house on a green lawn with flowering gardens, trees and sea view"></div>

  <section class="features">
    <ul class="feature-list left">
      <li>No Floor Time—Leads Sent<br>Directly to You</li>
      <li>E&amp;O Insurance included</li>
    </ul>
    <ul class="feature-list right">
      <li>All your listings showcased on<br>Homefinda.com</li>
      <li>Showing appointment solution</li>
    </ul>
  </section>

  <div class="pricing-band">
    <span>$350/month</span><span class="sep"></span>
    <span>No Office Time is Required</span><span class="sep"></span>
    <span>Virtual Office Solutions</span>
  </div>

  <div class="contact">
    <div>FOR MORE INFO VISIT</div>
    <div class="link">corvelliahomes.com/careers</div>
    <div>OR CALL <span class="phone">555.482.9167 ext. 204</span></div>
  </div>

  <div class="brand">
    <div class="brand-mark"></div>
    <div class="brand-name">CORVELLIA HOMES</div>
  </div>
</div>
</body>
</html>
```